Business Card design for Founder and CEO of new shoe company

I am looking for a business card design for my new shoe company called Strapwell.

I am launching the company this April. Strapwell shoes offers slip-on athletic and casual style shoes for men and women. The unique selling point of the brand is that all of our shoe exist without shoelaces. I have included a link to the website to offer additional information about the company, see product images, and gain inspiration for the design. You can use the store owner password "Strapwell" to access the website.

www.Strapwell.example

Thanks,
Dan Hollis

Target Market(s)

Active Men and Women ages 16-45

Industry/Entity Type

Business

Contact Information for Business Card

Dan Hollis
Founder and CEO
www.Strapwell.example
danhollis@Strapwell.example
888-555-0187 / 888-5STRAPW
Strapwell, LLC
2284 N Tamsin Ave
Chicago, IL 60699

Requirements
Must have
• Be able to quickly and easily tell that Strapwell is a shoe company from the business card

```html
<!DOCTYPE html>
<html lang="en">
<head>
<meta charset="utf-8">
<title>Strapwell Business Card</title>
<link rel="stylesheet" href="https://fonts.googleapis.com/css2?family=Open+Sans:wght@400;600;800&display=swap">
<style>
  :root {
    --page: #e4e4e4;
    --ink: #111111;
    --paper: #ffffff;
    --text: #1c1c1c;
    --muted: #3a3a3a;
    --pink: #d9489a;
    --navy: #3b3f9c;
    --sky: #3fb2de;
    --silver: #c9ccd1;
  }
  html, body {
    margin: 0;
    width: 1200px;
    height: 900px;
    overflow: hidden;
    background: var(--page);
    font-family: "Open Sans", Arial, sans-serif;
  }
  .canvas {
    position: relative;
    width: 1200px;
    height: 900px;
  }
  .card {
    position: absolute;
    left: 300px;
    width: 600px;
    height: 343px;
    border-radius: 18px;
    overflow: hidden;
    box-shadow: 0 6px 18px rgba(0,0,0,0.18);
  }
  .card-back {
    top: 90px;
    background: var(--ink);
    display: flex;
    align-items: center;
    justify-content: center;
  }
  .card-back .brand {
    color: var(--paper);
    font-size: 64px;
    font-weight: 400;
    letter-spacing: 1px;
  }
  .card-front {
    top: 467px;
    background: var(--paper);
  }
  .card-front svg.swoosh {
    position: absolute;
    inset: 0;
  }
  .product-photo {
    position: absolute;
    border-radius: 14px;
  }
  .photo-slipons {
    left: 22px; top: 140px; width: 210px; height: 110px;
    background: linear-gradient(100deg, var(--pink) 0%, var(--navy) 45%, var(--silver) 75%, var(--navy) 100%);
  }
  .photo-cap {
    left: 248px; top: 88px; width: 130px; height: 92px;
    background: radial-gradient(circle at 45% 40%, #ffffff 0%, #ececec 60%, #d7d7d7 100%);
    border-radius: 50% 50% 20px 20px;
  }
  .photo-runners {
    left: 392px; top: 14px; width: 192px; height: 96px;
    background: linear-gradient(100deg, var(--sky) 0%, var(--silver) 40%, var(--sky) 70%, #dfe3e8 100%);
  }
  .front-brand {
    position: absolute;
    left: 40px;
    top: 262px;
    font-size: 40px;
    font-weight: 400;
    color: var(--ink);
    letter-spacing: 0.5px;
  }
  .contact {
    position: absolute;
    right: 28px;
    top: 140px;
    text-align: right;
    color: var(--text);
  }
  .contact .name {
    font-size: 22px;
    font-weight: 800;
    margin: 0;
    letter-spacing: 0.5px;
  }
  .contact .title {
    font-size: 12px;
    margin: 0 0 6px;
    color: var(--muted);
  }
  .contact .line {
    font-size: 12.5px;
    font-weight: 600;
    margin: 1px 0;
    display: flex;
    justify-content: flex-end;
    align-items: center;
    gap: 6px;
  }
  .contact .line svg { width: 11px; height: 11px; }
  .contact .address {
    font-size: 12.5px;
    font-weight: 600;
    margin: 6px 0 0;
    line-height: 1.35;
  }
</style>
</head>
<body>
<main class="canvas">
  <section class="card card-back" aria-label="Card back">
    <span class="brand">Strapwell</span>
  </section>

  <section class="card card-front" aria-label="Card front">
    <div class="product-photo photo-slipons" role="img" aria-label="Pink and blue laceless slip-on sneakers"></div>
    <div class="product-photo photo-cap" role="img" aria-label="White baseball cap with brand name"></div>
    <div class="product-photo photo-runners" role="img" aria-label="Blue and silver athletic shoes"></div>

    <svg class="swoosh" viewBox="0 0 600 343" width="600" height="343" aria-hidden="true">
      <path d="M0 300 C 120 350, 250 330, 320 250 C 380 170, 420 110, 600 95" fill="none" stroke="var(--ink)" stroke-width="9"/>
      <path d="M0 320 C 140 360, 270 345, 340 262 C 400 185, 450 125, 600 120" fill="none" stroke="var(--ink)" stroke-width="3"/>
    </svg>

    <span class="front-brand">Strapwell</span>

    <div class="contact">
      <p class="name">DAN HOLLIS</p>
      <p class="title">Founder and CEO</p>
      <p class="line">888-555-0187 / 888-5STRAPW
        <svg viewBox="0 0 12 12"><path d="M2.5 1 L4.5 1 L5.2 3.6 L4 4.6 C4.6 6 6 7.4 7.4 8 L8.4 6.8 L11 7.5 L11 9.5 C11 10.3 10.3 11 9.5 11 C5 11 1 7 1 2.5 C1 1.7 1.7 1 2.5 1Z" fill="var(--ink)"/></svg>
      </p>
      <p class="line">danhollis@Strapwell.example
        <svg viewBox="0 0 12 12"><rect x="1" y="2.5" width="10" height="7" fill="none" stroke="var(--ink)" stroke-width="1.2"/><path d="M1 2.5 L6 6.5 L11 2.5" fill="none" stroke="var(--ink)" stroke-width="1.2"/></svg>
      </p>
      <p class="line">www.Strapwell.example
        <svg viewBox="0 0 12 12"><circle cx="6" cy="6" r="5" fill="none" stroke="var(--ink)" stroke-width="1.1"/><ellipse cx="6" cy="6" rx="2.2" ry="5" fill="none" stroke="var(--ink)" stroke-width="1"/><path d="M1 6 H11" stroke="var(--ink)" stroke-width="1"/></svg>
      </p>
      <p class="address">Strapwell, LLC 2284 N Tamsin Ave<br>Chicago, IL 60699</p>
    </div>
  </section>
</main>
</body>
</html>
```